We are a new towing and recovery company starting out in Calhan, CO. We do not want anything generic, we are looking to stand out. we will be doing towing for motorcycles to straight trucks we will have a rollback a 16-ton wrecker and a service vehicle with a wheel lift attached to tow small sized vehicles. We will also be doing roadside services which include lock-out, fuel delivery, jumpstarts, tire changes, and minor auto repair. we will be providing a quality and fast service also customer service will be one of main focuses.

Industry/Entity Type

Wheel

Contact Information for Business Card

Brindle Ridge Towing and Recovery, Dale Hoskin, Owner, 48210 S. Ferrow Road, Kestrel Bend, CO 80000 555-218-6497 Phone 555-218-6532 Fax www.brindleridgetow.example

```html
<!DOCTYPE html>
<html lang="en">
<head>
<meta charset="utf-8">
<title>Brindle Ridge Towing and Recovery – Business Card</title>
<link rel="stylesheet" href="https://fonts.googleapis.com/css2?family=Open+Sans:wght@400;600;700&display=swap">
<style>
  :root {
    --backdrop: #2b2b2b;
    --card-top: #ececec;
    --card-white: #ffffff;
    --text-grey: #58595b;
    --icon-grey: #5e5f61;
    --brand-blue: #1f5c99;
    --green-dark: #06844a;
    --green-mid: #0aab4e;
    --green-light: #8cc63f;
    --blue-light: #1b7bc4;
    --blue-dark: #2a3b8f;
    --art-yellow: #e9d84a;
    --art-blue: #3c6fb0;
  }
  * { margin: 0; padding: 0; box-sizing: border-box; }
  html, body {
    width: 1200px; height: 999px; overflow: hidden;
    background: var(--backdrop);
    font-family: "Open Sans", Arial, sans-serif;
  }
  .card {
    position: absolute; left: 75px; top: 200px;
    width: 1050px; height: 600px;
    background: linear-gradient(to bottom, var(--card-top) 0%, var(--card-white) 28%, var(--card-white) 100%);
    overflow: hidden;
  }
  .truck-art {
    position: absolute; left: 76px; top: 188px;
    width: 346px; height: 104px;
    border-radius: 40px 50px 30px 30px;
    background: linear-gradient(90deg, #e8e8ec 0%, var(--art-blue) 38%, var(--art-yellow) 62%, #d9d9d9 100%);
    opacity: .85;
  }
  .brand-name {
    position: absolute; left: 50px; top: 308px; width: 410px;
    text-align: center;
    color: var(--brand-blue);
    font-weight: 700; font-size: 34px; line-height: 46px;
  }
  .contact-block { position: absolute; left: 570px; top: 0; }
  .person-name {
    position: absolute; left: 2px; top: 148px; white-space: nowrap;
    font-size: 45px; font-weight: 400; color: var(--text-grey);
  }
  .person-role {
    position: absolute; left: 2px; top: 208px;
    font-size: 24px; color: var(--text-grey);
  }
  .detail {
    position: absolute; left: 39px; white-space: nowrap;
    font-size: 26px; line-height: 35px; color: var(--text-grey);
  }
  .detail-address { top: 288px; }
  .detail-phone { top: 374px; }
  .detail-fax { top: 409px; }
  .detail-web { top: 444px; }
  .icon { position: absolute; left: -7px; fill: var(--icon-grey); }
  .icon-pin { top: 290px; }
  .icon-phone { top: 383px; }
  .icon-fax { top: 418px; }
  .icon-web { top: 452px; }
  .footer-bands { position: absolute; left: 0; top: 550px; }
</style>
</head>
<body>
  <div class="card">
    <div class="truck-art" role="img" aria-label="Illustration of a white wheel-lift tow truck and a yellow wrecker truck"></div>
    <div class="brand-name">Brindle Ridge Towing<br>and Recovery</div>

    <div class="contact-block">
      <div class="person-name">Dale Hoskin</div>
      <div class="person-role">Owner</div>

      <svg class="icon icon-pin" width="26" height="40" viewBox="0 0 26 40" aria-hidden="true">
        <path d="M13 1C6.4 1 1 6.3 1 12.9 1 21 13 38 13 38s12-17 12-25.1C25 6.3 19.6 1 13 1zm0 17a5 5 0 1 1 0-10 5 5 0 0 1 0 10z"/>
      </svg>
      <div class="detail detail-address">48210 S. Ferrow Road,<br>Kestrel Bend, CO 80000</div>

      <svg class="icon icon-phone" width="24" height="24" viewBox="0 0 24 24" aria-hidden="true">
        <path d="M6.6 10.8c1.4 2.8 3.8 5.1 6.6 6.6l2.2-2.2c.3-.3.7-.4 1-.2 1.1.4 2.3.6 3.600.6.6 0 1 .4 1 1V20c0 .6-.4 1-1 1C10.6 21 3 13.4 3 4c0-.6.4-1 1-1h3.5c.6 0 1 .4 1 1 0 1.3.2 2.5.6 3.6.1.3 0 .7-.2 1L6.6 10.8z"/>
        <path d="M14 2.5a8 8 0 0 1 7.5 7.5h-1.8A6.2 6.2 0 0 0 14 4.3zM14 6a4.5 4.5 0 0 1 4 4h-1.8A2.7 2.7 0 0 0 14 7.8z"/>
      </svg>
      <div class="detail detail-phone">555-218-6497</div>

      <svg class="icon icon-fax" width="24" height="24" viewBox="0 0 24 24" aria-hidden="true">
        <path d="M7 2h10v7H7z"/>
        <path d="M4 10h16a2 2 0 0 1 2 2v8H2v-8a2 2 0 0 1 2-2zm3 4v2h10v-2z"/>
      </svg>
      <div class="detail detail-fax">555-218-6532</div>

      <svg class="icon icon-web" width="24" height="24" viewBox="0 0 24 24" aria-hidden="true">
        <circle cx="12" cy="12" r="11"/>
        <g fill="none" stroke="#ffffff" stroke-width="1.4">
          <ellipse cx="12" cy="12" rx="4.5" ry="10"/>
          <path d="M12 2v20M2 12h20M3.5 7h17M3.5 17h17"/>
        </g>
      </svg>
      <div class="detail detail-web">www.brindleridgetow.example</div>
    </div>

    <svg class="footer-bands" width="1050" height="50" viewBox="0 0 1050 50" aria-hidden="true">
      <defs>
        <linearGradient id="greenBand" x1="0" y1="0" x2="1" y2="0">
          <stop offset="0" stop-color="var(--green-dark)"/>
          <stop offset="0.6" stop-color="var(--green-mid)"/>
          <stop offset="1" stop-color="var(--green-light)"/>
        </linearGradient>
        <linearGradient id="blueBand" x1="0" y1="0" x2="0" y2="1">
          <stop offset="0" stop-color="var(--blue-light)"/>
          <stop offset="1" stop-color="var(--blue-dark)"/>
        </linearGradient>
      </defs>
      <polygon points="0,0 623,0 590,50 0,50" fill="url(#greenBand)"/>
      <polygon points="643,0 1050,0 1050,50 609,50" fill="url(#blueBand)"/>
    </svg>
  </div>
</body>
</html>
```